Dunmore Partners Brochure Design

Design a brochure for Dunmore Partners, with a focus on the three key areas of the business:
- Business Advisory (consulting);
- Turnaround;
- Business Valuations.

Details in relation to the above available at www.dunmorepartners-example.com

The aim of the document is to have something which works in a digital and physical form. The brochure should have each of the above areas on a separate A4 page so as to enable them to be presented digitally as stand alone brochures. Alternative designs which achieve the same will be accepted, I.e. Multiple brochures, one for whole of business and one for each business area.

Should also have a brief bio on Colin Brady and Dunmore Partners, also on a separate page or included in separate brochures if this approach is taken.

Industry/Entity Type

Digital

Requirements
Must have
• Please ensure that design flows from website.

```html
<!DOCTYPE html>
<html lang="en">
<head>
<meta charset="utf-8">
<title>Dunmore Partners – Brochure Pages</title>
<link href="https://fonts.googleapis.com/css2?family=Open+Sans:wght@300;400;600&display=swap" rel="stylesheet">
<style>
  :root {
    --page: #ffffff;
    --canvas: #ffffff;
    --brand-blue: #3f9cc8;
    --heading-blue: #3a8fc2;
    --logo-orange: #f0962a;
    --ink: #3a3a3a;
    --band-text: #ffffff;
  }
  * { margin: 0; padding: 0; box-sizing: border-box; }
  html, body { width: 1200px; height: 900px; overflow: hidden; background: var(--canvas); }
  body { position: relative; font-family: "Open Sans", Arial, sans-serif; color: var(--ink); }

  .page { position: absolute; background: var(--page); overflow: hidden; }
  .page--consulting { left: 80px; top: 80px; width: 495px; height: 350px; }
  .page--turnaround { left: 575px; top: 462px; width: 491px; height: 348px; }

  .photo { position: absolute; }
  .photo--meeting { left: 575px; top: 80px; width: 491px; height: 350px;
    background: linear-gradient(135deg, #e9ecef 0%, #d6d9dc 35%, #5d6066 55%, #cfd2d5 75%, #eef0f2 100%); }
  .photo--tablet { left: 80px; top: 462px; width: 495px; height: 348px;
    background: radial-gradient(ellipse at 35% 45%, #c9d8e4 0%, #7e93a6 35%, #3b4a5c 70%, #1f2a38 100%); }

  .brand { position: absolute; display: flex; align-items: center; gap: 5px;
    font-size: 10px; font-weight: 400; color: var(--heading-blue); }
  .brand__mark { width: 12px; height: 12px; background: var(--logo-orange); }
  .page--consulting .brand { left: 352px; top: 24px; }
  .page--turnaround .brand { left: 370px; top: 24px; }

  .page__title { position: absolute; font-weight: 300; font-size: 20px; color: var(--heading-blue); }
  .page--consulting .page__title { left: 23px; top: 54px; }
  .page--turnaround .page__title { left: 40px; top: 49px; }

  .intro-band { position: absolute; background: var(--brand-blue); color: var(--band-text);
    font-weight: 300; font-size: 9.6px; line-height: 13px; }
  .page--consulting .intro-band { left: 0; top: 97px; width: 452px; height: 63px; padding: 9px 14px 0 22px; }
  .page--turnaround .intro-band { left: 23px; top: 95px; width: 468px; height: 71px; padding: 4px 12px 0 19px; }

  .column { position: absolute; }
  .page--consulting .column--left { left: 23px; top: 170px; width: 212px; }
  .page--consulting .column--right { left: 241px; top: 168px; width: 212px; }
  .page--turnaround .column--left { left: 40px; top: 176px; width: 212px; }
  .page--turnaround .column--right { left: 258px; top: 176px; width: 214px; }

  .section__heading { font-weight: 300; font-size: 10.5px; color: var(--heading-blue); margin-bottom: 6px; }
  .section__body { font-size: 5.2px; line-height: 7px; margin-bottom: 10px; }
  .section__body p { margin-bottom: 4px; }
  .section__list { list-style: none; }
  .section__list--bullets { list-style: disc; padding-left: 14px; }
</style>
</head>
<body>

<section class="page page--consulting">
  <div class="brand"><span class="brand__mark"></span>Dunmore Partners</div>
  <h1 class="page__title">Consulting Services</h1>
  <p class="intro-band">Dunmore Partners aim to work with businesses to critically analyse opportunities or to resolve a specific problem. Our consultants work with management to identify the risks &amp; break these risks into manageable problems which can then be addressed. Our business consulting services can assist your business in navigating risk and overcoming your obstacles.</p>

  <div class="column column--left">
    <h2 class="section__heading">Structuring</h2>
    <div class="section__body">
      <p>Choosing the right structure is critical to the long-term effectiveness and efficiencies of a business or transaction. Getting it wrong can have serious tax and asset protection ramifications. We provide advice based upon a strong understanding of the business and/or transaction. This will ensure that we provide a solution which mitigates the risks as identified.</p>
    </div>
    <h2 class="section__heading">Solvency Support</h2>
    <div class="section__body">
      <p>We provide businesses and individuals facing financial difficulties with independent impartial advice. With a wealth of experience in restructuring, refinancing and successful asset divestments, we can help guide a company through what can be very difficult time for businesses and business owners. This advice may include:</p>
      <ul class="section__list">
        <li>Assisting directors understand solvency and their obligations;</li>
        <li>Preparing providing directors independent advice through an administration process;</li>
        <li>Providing directors with formal insolvency options available;</li>
        <li>Designing a Deed of Company arrangement or other informal arrangement.</li>
      </ul>
    </div>
  </div>

  <div class="column column--right">
    <h2 class="section__heading">Due Diligence</h2>
    <div class="section__body">
      <p>Financial transactions invariably require a level of due diligence, this process covers a range of areas, including but not limited to:</p>
      <ul class="section__list">
        <li>• Operational Due Diligence;</li>
        <li>• Legal Due Diligence;</li>
        <li>• Financial Due Diligence;</li>
      </ul>
      <p>&nbsp;</p>
      <p>The scope of these works will vary between transactions. Dunmore Partners' management consultants can assist you through this process, providing specific advice in relation to financial due diligence and providing guidance with legal and operational due diligence.</p>
      <p>If you have any questions in relation to the above items or anything else which you believe we could be of assistance with please contact us to confidentially discuss your specific requirements.</p>
    </div>
  </div>
</section>

<div class="photo photo--meeting" role="img" aria-label="Overhead photo of two business people reviewing documents at a white desk"></div>
<div class="photo photo--tablet" role="img" aria-label="Photo of a businessman in a suit using a stylus on a tablet"></div>

<section class="page page--turnaround">
  <div class="brand"><span class="brand__mark"></span>Dunmore Partners</div>
  <h1 class="page__title">Turnaround Advisors</h1>
  <p class="intro-band">Often, external factors can result in a business being at risk of failure. In these situations, Dunmore Partners' turnaround advisors are qualified to identify the critical issues faced by businesses and can provide assistance in resolving these issues. Through expert business management we assess the position of the company and prepare a plan to move forward. This plan is likely to include some or all of the following processes:</p>

  <div class="column column--left">
    <h2 class="section__heading">Negotiation with Tax Office and other Creditors</h2>
    <div class="section__body">
      <p>With considerable experience negotiating with creditors, in particular the Tax Office, we can assist your business in dealing with the stressful process of managing creditors during times of stress.</p>
    </div>
    <h2 class="section__heading">Cash flow management</h2>
    <div class="section__body">
      <p>We understand the pressures of running a business which is short on cash. We can assist with the implementation of processes to manage cash flows, as well as provide you with tools to maximize the cash you have access to.</p>
    </div>
    <h2 class="section__heading">Finance and working capital</h2>
    <div class="section__body">
      <p>We can assist businesses assess their working capital requirements, assist with the identification of appropriate financiers, and assist with preparing the required financial and other information to apply for finance.</p>
    </div>
  </div>

  <div class="column column--right">
    <h2 class="section__heading">Solvency Support</h2>
    <div class="section__body">
      <p>The specialist turnaround advisors at Dunmore Partners can provide businesses and individuals facing financial difficulties with independent, impartial advice on solvency. With a wealth of experience in restructuring, refinancing and successful asset divestments, we can help guide a business through what can be very difficult time for businesses and business owners.<br>This advice may include:</p>
      <ul class="section__list section__list--bullets">
        <li>Assisting directors understand solvency and their obligations;</li>
        <li>Preparing providing directors independent advice through an administration process;</li>
        <li>Providing directors with formal insolvency options available;</li>
        <li>Designing a Deed of Company arrangement or other informal arrangement.</li>
      </ul>
      <p>&nbsp;</p>
      <p>For honest and helpful turnaround management services, please contact Dunmore Partners today. Available Sydney wide, we're ready to work with your business.</p>
    </div>
  </div>
</section>

</body>
</html>
```